Brightwater Facility Partners Business card

We wish to have a professional Business card to present to large Corporate CEO's ASAP.

Our web site helps explain our business www.brightwaterfp.org

Brightwater Facility Partners was established after we discovered how difficult it is to organise outsourced services while heading up a business or company.

We act as a facilitator for businesses who don't have the desire, expertise or recourses to manage their own systems and meet all their requirements.

We provide an all in one facility management solution for all types of businesses. We manage schedules, contractors and costs on behalf of businesses and their needs and wants.

Having an extensive network ensures we are able to connect businesses with the right service providers.

Target Market(s)

Company CEO

Industry/Entity Type

Business

Font styles to use
Sans Serif

Colors
33a6d7
f9fdfe
0355a3

Requirements
Must have
• professional design
Nice to have
• colours to match logo

```html
<!DOCTYPE html>
<html lang="en">
<head>
<meta charset="utf-8">
<title>Brightwater Facility Partners – Business Card</title>
<link rel="stylesheet" href="https://fonts.googleapis.com/css2?family=Lato:wght@400;700&display=swap">
<style>
  :root {
    --stage: #2e2e2e;
    --brand-blue: #0355a3;
    --brand-sky: #33a6d7;
    --card-white: #f9fdfe;
    --ink: #1c1c1c;
    --ink-soft: #3a3a3a;
    --navy-deep: #0a3f86;
  }
  * { margin: 0; padding: 0; box-sizing: border-box; }
  html, body {
    width: 1200px; height: 997px; overflow: hidden;
    background: var(--stage);
    font-family: "Lato", Arial, sans-serif;
  }
  .stage {
    position: relative; width: 1200px; height: 997px;
    display: flex; align-items: center; justify-content: center; gap: 60px;
  }
  .card {
    position: relative; width: 520px; height: 300px;
    border-radius: 22px; overflow: hidden;
  }
  /* Back of card */
  .card--back {
    background: linear-gradient(160deg, #1f6fd0 0%, var(--brand-blue) 55%, var(--navy-deep) 100%);
  }
  .card--back .back-tagline {
    position: absolute; right: 40px; top: 112px;
    font-size: 11px; letter-spacing: 1.5px; text-transform: uppercase;
    color: var(--ink); text-align: right;
  }
  .card--back .back-name {
    position: absolute; right: 40px; top: 130px;
    font-size: 21px; font-weight: 700; letter-spacing: 1px; text-transform: uppercase;
    color: var(--ink); text-align: right;
  }
  /* Front of card */
  .card--front { background: var(--card-white); }
  .brand {
    position: absolute; left: 46px; top: 52px;
    display: flex; align-items: center; gap: 12px;
  }
  .brand__dot {
    width: 30px; height: 30px; border-radius: 50%;
    background: var(--brand-blue);
  }
  .brand__name {
    font-size: 19px; font-weight: 700; letter-spacing: 1px; text-transform: uppercase;
    color: var(--brand-blue); line-height: 1.05;
  }
  .person {
    position: absolute; right: 36px; top: 122px;
    font-size: 20px; letter-spacing: 1px; text-transform: uppercase;
    color: var(--brand-blue);
  }
  .person__last { font-weight: 700; color: var(--navy-deep); }
  .rule { position: absolute; height: 2px; background: var(--ink); }
  .rule--name { left: 210px; right: 30px; top: 152px; }
  .rule--contact { left: 30px; width: 250px; top: 196px; }
  .contact {
    position: absolute; left: 30px; top: 206px;
    list-style: none; display: flex; flex-direction: column; gap: 9px;
  }
  .contact__item {
    display: flex; align-items: center; gap: 10px;
    font-size: 14px; font-weight: 700; color: var(--ink-soft);
  }
  .contact__icon { width: 16px; height: 16px; flex: none; }
</style>
</head>
<body>
<main class="stage">
  <section class="card card--back" aria-label="Business card, back">
    <p class="back-tagline">Management Solutions</p>
    <p class="back-name">Brightwater Facility Partners</p>
  </section>

  <section class="card card--front" aria-label="Business card, front">
    <div class="brand">
      <span class="brand__dot"></span>
      <p class="brand__name">Brightwater<br>Facility Partners</p>
    </div>

    <p class="person">Daniel <span class="person__last">Hartley</span></p>
    <div class="rule rule--name"></div>
    <div class="rule rule--contact"></div>

    <ul class="contact">
      <li class="contact__item">
        <svg class="contact__icon" viewBox="0 0 16 16" aria-hidden="true">
          <path fill="#0355a3" d="M3 2h3l1 3-2 1a8 8 0 0 0 5 5l1-2 3 1v3a1 1 0 0 1-1 1A12 12 0 0 1 2 3a1 1 0 0 1 1-1z"/>
        </svg>
        0400 123 987
      </li>
      <li class="contact__item">
        <svg class="contact__icon" viewBox="0 0 16 16" aria-hidden="true">
          <g fill="none" stroke="#0355a3" stroke-width="2" stroke-linecap="round">
            <path d="M7 9l-2 2a2 2 0 0 1-3-3l2-2"/>
            <path d="M9 7l2-2a2 2 0 0 0-3-3L6 4"/>
            <path d="M6 10l4-4"/>
          </g>
        </svg>
        www.brightwaterfp.org
      </li>
      <li class="contact__item">
        <svg class="contact__icon" viewBox="0 0 16 16" aria-hidden="true">
          <rect x="1" y="3" width="14" height="10" rx="1" fill="#0355a3"/>
          <path d="M1.5 3.5L8 9l6.5-5.5" fill="none" stroke="#f9fdfe" stroke-width="1.3"/>
        </svg>
        daniel@brightwaterfp.org
      </li>
    </ul>
  </section>
</main>
</body>
</html>
```